Sliding banner

I need three sliding banners designed for my website korvalent.co.za - please take a look at the existing banner format.

The products items on the banner can be any product that is on the website - the size of the banner must remain the same - the design project is only for the sliding banner.

Regards

```html
<!DOCTYPE html>
<html lang="en">
<head>
<meta charset="utf-8">
<title>Power Up With No Power Outlet</title>
<link href="https://fonts.googleapis.com/css2?family=Open+Sans:wght@300;400;700&display=swap" rel="stylesheet">
<style>
  :root {
    --sky-deep: #4a9fd6;
    --sky-mid: #6fb4e2;
    --sky-light: #93c9ec;
    --title-blue: #3b97d6;
    --white: #ffffff;
    --badge-black: #1c1c1c;
    --product-light: #f4f4f4;
    --product-shade: #d9d9d9;
  }
  html, body {
    margin: 0;
    padding: 0;
    width: 1200px;
    height: 406px;
    overflow: hidden;
  }
  .banner {
    position: relative;
    width: 1200px;
    height: 406px;
    overflow: hidden;
    background: linear-gradient(180deg, var(--sky-deep) 0%, var(--sky-mid) 30%, var(--sky-light) 52%, var(--sky-mid) 75%, var(--sky-deep) 100%);
    font-family: "Open Sans", Arial, sans-serif;
  }
  .headline {
    position: absolute;
    left: 58px;
    top: 101px;
    width: 667px;
    height: 50px;
    margin: 0;
    background: var(--white);
    color: var(--title-blue);
    font-weight: 400;
    font-size: 35px;
    line-height: 50px;
    letter-spacing: 0.3px;
    padding-left: 14px;
    box-sizing: border-box;
    white-space: nowrap;
  }
  .tagline {
    position: absolute;
    left: 58px;
    top: 164px;
    width: 560px;
    margin: 0;
    color: var(--white);
    font-weight: 400;
    font-size: 19.5px;
    line-height: 24px;
    text-shadow: 0 1px 2px rgba(0, 60, 110, 0.25);
  }
  .product-stage {
    position: absolute;
    left: 726px;
    top: 31px;
    width: 412px;
    height: 412px;
    border-radius: 50%;
    background: var(--white);
    box-shadow: 0 0 12px rgba(0, 50, 100, 0.25);
  }
  .product-photo {
    position: absolute;
    left: 70px;
    top: 92px;
    width: 248px;
    height: 226px;
    border-radius: 60px 110px 100px 50px;
    background: linear-gradient(160deg, var(--product-light) 0%, var(--white) 45%, var(--product-shade) 100%);
    transform: rotate(18deg);
  }
  .price-badge {
    position: absolute;
    left: 1031px;
    top: 49px;
    width: 102px;
    height: 102px;
    border-radius: 50%;
    background: var(--badge-black);
    color: var(--white);
    text-align: center;
  }
  .price-badge svg {
    position: absolute;
    left: 0;
    top: 0;
  }
  .price-currency {
    position: absolute;
    left: 0;
    right: 0;
    top: 17px;
    font-weight: 700;
    font-size: 21px;
    line-height: 24px;
  }
  .price-amount {
    position: absolute;
    left: 0;
    right: 0;
    top: 46px;
    font-weight: 300;
    font-size: 19px;
    line-height: 24px;
  }
</style>
</head>
<body>
  <section class="banner">
    <h1 class="headline">POWER UP WITH NO POWER OUTLET</h1>
    <p class="tagline">Rechargeable battery for powering up your Mobile phone or Tablet when you can't find a power outlet.</p>

    <div class="product-stage">
      <div class="product-photo" role="img" aria-label="White cylindrical portable power bank with USB port"></div>
    </div>

    <div class="price-badge">
      <svg width="102" height="102" viewBox="0 0 102 102" aria-hidden="true">
        <circle cx="51" cy="51" r="43" fill="none" stroke="#ffffff" stroke-width="1.5"/>
      </svg>
      <span class="price-currency">$</span>
      <span class="price-amount">325.00</span>
    </div>
  </section>
</body>
</html>
```